Brightwave Reach - Business Card

We need a business card for a Social Media Marketing company that specializes in online marketing for small businesses in Canada using common Social Media platforms such as Pictora, Kinloop, Blinkit & Chirpo.

I have uploaded a copy of our logo which I would like utilized in the business card. We would like the business card to be modern yet classy design.

Our website is www.brightwavereach.ca

Industry/Entity Type

Marketing

Contact Information for Business Card

Email: info@brightwavereach.ca
Website: www.brightwavereach.ca
Telephone: 604-392-5108

Colors

Designer to choose colors to be used in the design.

Requirements
Must have
• Social Media icons on reverse
• Please add some designs with color.

```html
<!DOCTYPE html>
<html lang="en">
<head>
<meta charset="utf-8">
<title>Brightwave Reach – Business Card</title>
<link rel="stylesheet" href="https://fonts.googleapis.com/css2?family=Lato:wght@300;400;700;900&display=swap">
<style>
  :root {
    --backdrop: #c8bdf9;
    --front-card: #2c393d;
    --back-card: #0f0f0f;
    --brand-ink: #e6e6e1;
    --text-light: #e4e4e4;
    --rule: #5a5a5a;
    --icon-fill: #f4f4f4;
    --icon-glyph: #111111;
  }
  * { margin: 0; padding: 0; box-sizing: border-box; }
  html, body {
    width: 1200px;
    height: 1000px;
    overflow: hidden;
    background: var(--backdrop);
    font-family: "Lato", "Helvetica Neue", Arial, sans-serif;
  }
  .canvas {
    position: relative;
    width: 1200px;
    height: 1000px;
  }
  .card {
    position: absolute;
    left: 241px;
    width: 743px;
    height: 434px;
    box-shadow: 0 1px 2px rgba(0,0,0,0.25);
  }
  .card--front { top: 45px; background: var(--front-card); }
  .card--back  { top: 520px; height: 433px; background: var(--back-card); }

  .wordmark {
    position: absolute;
    display: flex;
    align-items: center;
    color: var(--brand-ink);
    font-weight: 900;
    text-transform: uppercase;
    line-height: 0.95;
    text-align: center;
    white-space: nowrap;
  }
  .wordmark__square {
    flex: none;
    background: var(--brand-ink);
  }
  .wordmark__name { display: block; }

  .card--front .wordmark {
    left: 0; right: 0; top: 168px;
    justify-content: center;
    gap: 14px;
    font-size: 54px;
    letter-spacing: 1px;
  }
  .card--front .wordmark__square { width: 20px; height: 20px; }

  .card--back .wordmark {
    left: 20px; width: 320px; top: 190px;
    justify-content: center;
    gap: 10px;
    font-size: 37px;
    letter-spacing: 0.5px;
  }
  .card--back .wordmark__square { width: 15px; height: 15px; }

  .divider {
    position: absolute;
    left: 361px;
    top: 64px;
    width: 1px;
    height: 310px;
    background: var(--rule);
  }

  .tagline {
    position: absolute;
    left: 387px;
    top: 94px;
    color: var(--text-light);
    font-weight: 300;
    font-size: 23px;
    line-height: 34px;
    text-transform: uppercase;
  }

  .contact-list {
    position: absolute;
    left: 387px;
    top: 231px;
    width: 311px;
    list-style: none;
    border-top: 1px solid var(--rule);
  }
  .contact-list__item {
    display: flex;
    align-items: center;
    height: 48px;
    border-bottom: 1px solid var(--rule);
    color: var(--text-light);
    font-size: 19px;
    letter-spacing: 1.5px;
    white-space: nowrap;
  }
  .contact-list__icon {
    width: 25px;
    height: 25px;
    margin-left: 5px;
    margin-right: 23px;
    flex: none;
  }
</style>
</head>
<body>
<main class="canvas">

  <section class="card card--front" aria-label="Card front">
    <div class="wordmark">
      <span class="wordmark__square" aria-hidden="true"></span>
      <span class="wordmark__name">Brightwave<br>Reach</span>
    </div>
  </section>

  <section class="card card--back" aria-label="Card back">
    <div class="wordmark">
      <span class="wordmark__square" aria-hidden="true"></span>
      <span class="wordmark__name">Brightwave<br>Reach</span>
    </div>

    <div class="divider" aria-hidden="true"></div>

    <p class="tagline">Connecting your<br>business with<br>our community!</p>

    <ul class="contact-list">
      <li class="contact-list__item">
        <svg class="contact-list__icon" viewBox="0 0 25 25" aria-hidden="true">
          <rect width="25" height="25" rx="3" fill="var(--icon-fill)"/>
          <path d="M8 5.5c-1.2.4-2.2 1.6-2 3.2.6 4.6 5.4 9.8 10.3 10.8 1.5.3 2.7-.6 3.2-1.8l-3-2.6-1.7 1.4c-2-.9-3.8-2.8-4.7-4.8l1.5-1.6z" fill="none" stroke="var(--icon-glyph)" stroke-width="1.6" stroke-linejoin="round"/>
        </svg>
        <span>604-392-5108</span>
      </li>
      <li class="contact-list__item">
        <svg class="contact-list__icon" viewBox="0 0 25 25" aria-hidden="true">
          <rect width="25" height="25" rx="3" fill="var(--icon-fill)"/>
          <rect x="4" y="7" width="17" height="11" fill="none" stroke="var(--icon-glyph)" stroke-width="1.4"/>
          <path d="M4 7l8.5 6.5L21 7M4 18l6-5.5M21 18l-6-5.5" fill="none" stroke="var(--icon-glyph)" stroke-width="1.2"/>
        </svg>
        <span>info@brightwavereach.ca</span>
      </li>
      <li class="contact-list__item">
        <svg class="contact-list__icon" viewBox="0 0 25 25" aria-hidden="true">
          <rect width="25" height="25" rx="3" fill="var(--icon-fill)"/>
          <text x="12.5" y="15.5" text-anchor="middle" font-family="Lato, Arial, sans-serif" font-size="8" font-weight="700" fill="var(--icon-glyph)">www</text>
        </svg>
        <span>www.brightwavereach.ca</span>
      </li>
    </ul>
  </section>

</main>
</body>
</html>
```